Business Cards Design for the electrical wholesaler: clean bold dynamic :)

We need a business card design that would follow our latest brand guidelines. As an electrical wholesaler we want to bring a fresh look and feel into the industry. The design should be clean bold and dynamic. It should come alive with the renewed energy of our green colour. Our grey colour should keep things balanced and complement the notion of maturity and responsibility. We employ Lato as a corporate font however are not bound by this font and we’re open to interpretation here.

Target Market(s)

Electrical contractors

Industry/Entity Type

Business

Contact Information for Business Card

Logo
Name & Surname: Olena Dovbush
Job Title: Director of Marketing
Email: helen.dovbush@mailvane.example
Cell phone: XXX.XXX.XXXX
Address: 20917 - 87 Ave. Edmonton, AB, Canada. T6K 2R8
Business Phone: 780.555.0187
Website: www.qorvil.example

Font styles to use
Other font styles liked:
• Lato

Requirements
Must have
• Logo & website
Nice to have
• Brand elements - some of them you may find in the attached Brand Guidelines (e.g. three lines on the background signifying "W")

```html
<!DOCTYPE html>
<html lang="en">
<head>
<meta charset="utf-8">
<title>Qorvil Business Card</title>
<link rel="stylesheet" href="https://fonts.googleapis.com/css2?family=Lato:wght@400;700;900&display=swap">
<style>
  :root {
    --bg-light: #9a9d9e;
    --bg-dark: #55585a;
    --card-dark: #1b1d1e;
    --card-dark-edge: #2a2d2e;
    --brand-green: #8dc63f;
    --brand-green-deep: #7cb936;
    --brand-grey: #4d4e50;
    --text-light: #f2f2f2;
    --rule: #3a3d3f;
  }
  * { margin: 0; padding: 0; box-sizing: border-box; }
  html, body { width: 1200px; height: 1000px; overflow: hidden; }
  body {
    background: radial-gradient(ellipse at 45% 40%, var(--bg-light) 0%, var(--bg-dark) 100%);
    font-family: "Lato", sans-serif;
    position: relative;
  }
  .card {
    position: absolute;
    left: 330px;
    width: 540px;
    height: 300px;
    overflow: hidden;
    box-shadow: 0 6px 18px rgba(0,0,0,0.35);
  }
  .card-front {
    top: 180px;
    background: linear-gradient(135deg, var(--card-dark-edge) 0%, var(--card-dark) 60%);
    color: var(--text-light);
  }
  .card-back {
    top: 510px;
    background: linear-gradient(120deg, var(--brand-green) 55%, var(--brand-green-deep) 100%);
  }
  .side-tab { position: absolute; left: 0; top: 100px; }
  .title-row {
    position: absolute;
    left: 60px;
    top: 42px;
    font-weight: 700;
    font-size: 22px;
    color: var(--brand-green);
    letter-spacing: 0.2px;
  }
  .title-row .divider { margin: 0 14px; font-weight: 400; }
  .title-rule {
    position: absolute;
    left: 100px;
    right: 0;
    top: 90px;
    height: 3px;
    background: var(--rule);
    box-shadow: 0 1px 0 #000;
  }
  .contact-list {
    position: absolute;
    left: 130px;
    top: 112px;
    list-style: none;
    font-size: 16px;
    line-height: 25px;
  }
  .contact-list li { display: flex; align-items: center; gap: 12px; }
  .contact-list .bullet {
    width: 8px; height: 8px; border-radius: 50%;
    background: var(--brand-green);
    flex: none;
  }
  .address {
    position: absolute;
    right: 28px;
    bottom: 34px;
    text-align: right;
    font-size: 15px;
    font-style: normal;
    line-height: 28px;
    color: var(--brand-green);
  }
  .brand {
    position: absolute;
    left: 50%;
    top: 50%;
    transform: translate(-50%, -50%);
    display: flex;
    align-items: center;
    gap: 18px;
  }
  .brand-dot {
    width: 44px; height: 44px; border-radius: 50%;
    background: var(--brand-grey);
  }
  .brand-name {
    font-weight: 700;
    font-size: 68px;
    color: var(--brand-grey);
    letter-spacing: 1px;
  }
</style>
</head>
<body>
  <section class="card card-front">
    <svg class="side-tab" width="40" height="130" viewBox="0 0 40 130" aria-hidden="true">
      <polygon points="0,0 22,0 36,16 36,114 22,130 0,130" fill="none" stroke="var(--brand-green)" stroke-width="1"/>
      <polygon points="0,6 18,6 30,19 30,111 18,124 0,124" fill="var(--brand-green)"/>
    </svg>
    <div class="title-row">
      <span class="person-name">Olena Dovbush</span><span class="divider">|</span><span class="job-title">Director of Marketing</span>
    </div>
    <div class="title-rule"></div>
    <ul class="contact-list">
      <li><span class="bullet"></span>helen.dovbush@mailvane.example</li>
      <li><span class="bullet"></span>Work: 780.555.0187</li>
      <li><span class="bullet"></span>Cell: 780.555.0142</li>
      <li><span class="bullet"></span>www.qorvil.example</li>
    </ul>
    <address class="address">
      20917 - 87 Ave.<br>Edmonton, AB, Canada. T6K 2R8
    </address>
  </section>

  <section class="card card-back">
    <div class="brand">
      <span class="brand-dot"></span>
      <span class="brand-name">Qorvil</span>
    </div>
  </section>
</body>
</html>
```